Elegant Africa map and cards for a board game

This project is for the design of the board of a game and the playing cards.
The game is Called Velumi Games. Like the hexaland, players take a turn to move their pawns around a board based on the values of the thrown dice.

Players start playing around the map and to win the game they jump to the pyramid when they've achieved all objectives.

The design requirement is described in the following document :
https://files.draftlyhub.net/sheet/r/8XPQW2LmTrzeHbc4Yfa9_Nd3KLoPsvJqUw5tR_Ew/view?mode=public

Font styles to use
Script

Requirements
Must have
• - surrounding frame with an African design
- Africa map with race tracks
- a pyramid to the left of the map
- the back design of playing cards (see attached file: Velumi game - design)
Nice to have
• - a design for the Rules/guide document

```html
<!DOCTYPE html>
<html lang="en">
<head>
<meta charset="utf-8">
<title>Velumi Games – Region Cards</title>
<link rel="stylesheet" href="https://fonts.googleapis.com/css2?family=Source+Serif+4:opsz,wght@8..60,400;8..60,600&display=swap">
<style>
  :root {
    --page: #ffffff;
    --frame: #0d0d0d;
    --teal: #5bb0a8;
    --teal-deep: #4aa39c;
    --plum: #85577b;
    --plum-deep: #74466b;
    --ink-light: #ffffff;
  }
  * { box-sizing: border-box; margin: 0; padding: 0; }
  html, body {
    width: 1200px; height: 1200px; overflow: hidden;
    background: var(--page);
  }
  .canvas {
    position: relative; width: 1200px; height: 1200px;
    font-family: "Source Serif 4", Georgia, serif;
  }
  .card {
    position: absolute; top: 263px;
    width: 476px; height: 674px;
    border: 7px solid var(--frame);
    overflow: hidden;
    color: var(--ink-light);
  }
  .card--kenya { left: 123px; background: radial-gradient(ellipse at 35% 25%, var(--teal) 0%, var(--teal-deep) 60%, var(--teal) 100%); }
  .card--algeria { left: 634px; background: radial-gradient(ellipse at 35% 25%, var(--plum) 0%, var(--plum-deep) 60%, var(--plum) 100%); }

  .card__title {
    position: absolute; top: 66px; left: 0; right: 0;
    text-align: center; font-weight: 400; font-size: 80px; line-height: 1;
  }
  .card__rule {
    position: absolute; top: 166px; left: 50%;
    width: 160px; height: 3px; margin-left: -80px;
    background: var(--ink-light);
  }
  .card__region {
    position: absolute; top: 186px; left: 0; right: 0;
    text-align: center; font-size: 28px; line-height: 1.2;
  }
  .card__map {
    position: absolute; top: 246px; left: 70px;
    width: 320px; height: 340px;
    border-radius: 40% 44% 30% 34% / 22% 30% 70% 66%;
    opacity: .92;
  }
  .card--kenya .card__map {
    background: linear-gradient(165deg, #5e4a72 0%, #5e4a72 18%, #d2c86c 34%, #d98a3a 56%, #3f9b98 70%, #d9503a 92%);
  }
  .card--algeria .card__map {
    background: linear-gradient(165deg, #6a3560 0%, #6a3560 18%, #d6a45a 34%, #e06a30 56%, #4f8a8c 70%, #e0402e 92%);
  }
  .card__pointer {
    position: absolute; inset: 0; width: 100%; height: 100%;
    pointer-events: none;
  }
  .card__pointer path {
    fill: none; stroke: var(--ink-light); stroke-width: 3; stroke-linecap: round; stroke-linejoin: round;
  }
  .card__band {
    position: absolute; left: 0; right: 0; bottom: 0; height: 28px;
    background: linear-gradient(90deg, #6a4a80, #e07a3a, #d8c86a, #4aa7a0, #e0503a, #d8c86a, #6a4a80);
    opacity: .85;
  }
  .card__brand {
    position: absolute; bottom: 0; left: 151px;
    width: 160px; height: 54px;
    background: var(--frame);
    display: flex; align-items: center; justify-content: center;
    font-size: 19px; font-weight: 600; color: var(--ink-light);
    letter-spacing: .5px;
  }
</style>
</head>
<body>
<main class="canvas">
  <article class="card card--kenya">
    <h1 class="card__title">Kenya</h1>
    <div class="card__rule"></div>
    <p class="card__region">Eastern Africa</p>
    <div class="card__map" role="img" aria-label="Watercolour map of Africa with country borders, coloured by region, Eastern Africa highlighted"></div>
    <svg class="card__pointer" viewBox="0 0 462 660" aria-hidden="true">
      <path d="M398 456 C372 450 346 438 328 423"/>
      <path d="M328 423 L342 424 M328 423 L333 436"/>
    </svg>
    <div class="card__band" role="img" aria-label="Colourful African triangle pattern border"></div>
    <div class="card__brand">Velumi Games</div>
  </article>

  <article class="card card--algeria">
    <h1 class="card__title">Algeria</h1>
    <div class="card__rule"></div>
    <p class="card__region">Northern Africa</p>
    <div class="card__map" role="img" aria-label="Watercolour map of Africa with country borders, coloured by region, Northern Africa highlighted"></div>
    <svg class="card__pointer" viewBox="0 0 462 660" aria-hidden="true">
      <path d="M81 232 C108 256 134 276 163 288"/>
      <path d="M163 288 L150 280 M163 288 L150 292"/>
    </svg>
    <div class="card__band" role="img" aria-label="Colourful African triangle pattern border"></div>
    <div class="card__brand">Velumi Games</div>
  </article>
</main>
</body>
</html>
```